The Gentle Moonlit Harbour Journey

This book accompanies a video workshop. The book explains who our guardian angels are, what is their purpose, how to connect with them for wisdom & guidance. How to manifest what we world like bring into our lives by asking the Angels. The book contains meditation exercises, lots of information and fun facts about how our angels give us messages and guidance and how to become more intuitive. How to use angel oracle cards to receive guidance from our angels.
I'm quite an upbeat, happy person, so the book is written very warmly and is a collection of all the information that out ther, drawn together neatly by me, with my own unique take on all things angelic. Along with personal stories and anecdotes about how and why I became interested in angels and what they have taught me. It's fun, fresh, lighthearted and modern. Not at all serious, just extremely uplifting and positive, so I would really like the cover to reflect this.

Target Market(s)

Anyone who is interested in angels. From my chatterloop page activity I find it is mostly women of all ages who are interested in angels

Font styles to use
Serif
Sans Serif
Script

Colors
ea8dbb
f04a50
e667a6
e34197
85abd2
886aae
b7a5cd
6b449b
fbee3e

Requirements
Must have
• A more feminine appeal
• Look quite modern & upbeat but also calming and open
• I would like it to look etherel in some way. I definitely dont want something that looks like a cartoon or clip art
Should not have
• No dark colours or sinister imagery. I don't want people to feel like thus can't do the & it's only special people who can connect with their angels
• No haunting imagery!

```html
<!DOCTYPE html>
<html lang="en">
<head>
<meta charset="utf-8">
<title>The Gentle Moonlit Harbour Journey – Book Cover</title>
<link href="https://fonts.googleapis.com/css2?family=Playfair+Display:wght@400&family=Courgette&family=Great+Vibes&display=swap" rel="stylesheet">
<style>
  :root {
    --stage: #ececec;
    --sky-deep: #85abd2;
    --sky-mid: #b9d3ec;
    --sky-pale: #f4f8fc;
    --ink-purple: #6b449b;
    --band-purple: #886aae;
    --band-light: #b7a5cd;
    --white: #ffffff;
  }
  * { margin: 0; padding: 0; box-sizing: border-box; }
  html, body {
    width: 922px; height: 1200px; overflow: hidden;
    background: var(--stage);
  }
  .cover {
    position: absolute;
    left: 151px; top: 56px;
    width: 620px; height: 1088px;
    background: var(--sky-pale);
    overflow: hidden;
  }
  .cover-art {
    position: absolute; inset: 0 0 231px 0;
    background:
      radial-gradient(ellipse 60% 40% at 50% 42%, rgba(255,255,255,0.95), rgba(255,255,255,0) 70%),
      radial-gradient(ellipse 40% 30% at 15% 30%, rgba(255,255,255,0.9), rgba(255,255,255,0) 70%),
      linear-gradient(180deg, var(--sky-deep) 0%, var(--sky-mid) 30%, var(--sky-pale) 70%, var(--sky-pale) 100%);
  }
  .tagline {
    position: absolute; top: 72px; left: 0; right: 0;
    padding-left: 150px; padding-right: 40px;
    font-family: "Playfair Display", serif;
    font-size: 20px; line-height: 1.3;
    color: var(--ink-purple);
    text-align: center;
  }
  .title-script {
    position: absolute; top: 600px; left: 0; right: 0;
    font-family: "Courgette", cursive;
    font-size: 104px; line-height: 1.1;
    color: var(--ink-purple);
    text-align: center;
    padding-left: 60px;
  }
  .subtitle {
    position: absolute; top: 768px; left: 0; right: 0;
    display: flex; align-items: center; justify-content: center; gap: 14px;
    padding-left: 60px;
    font-family: "Playfair Display", serif;
    font-size: 19px; letter-spacing: 1px;
    color: var(--ink-purple);
  }
  .subtitle .rule { width: 72px; height: 2px; background: var(--ink-purple); }
  .author-band {
    position: absolute; left: 0; right: 0; bottom: 0; height: 231px;
    background: var(--band-purple);
    border-top: 16px solid var(--band-light);
  }
  .author {
    position: absolute; left: 0; right: 0; top: 110px;
    font-family: "Great Vibes", cursive;
    font-size: 42px;
    color: var(--white);
    text-align: center;
  }
</style>
</head>
<body>
  <main class="cover">
    <div class="cover-art" role="img" aria-label="Illustration of a winged angel in a white dress with a halo, rising through a soft blue sky with white clouds"></div>
    <p class="tagline">Connect with your angels<br>bring love, healing and divine<br>guidance to every area of your life</p>
    <h1 class="title-script">Moonlit</h1>
    <p class="subtitle"><span class="rule"></span>GENTLE HARBOUR JOURNEY<span class="rule"></span></p>
    <footer class="author-band">
      <p class="author">Rosalind Avery</p>
    </footer>
  </main>
</body>
</html>
```